New Website design 2024: Harbor Ridge Sealworks, Inc.

1. Who we are: At Harbor Ridge Sealworks Inc, our mission is to provide our clients with comprehensive firestop and seismic expansion joint solutions that ensure the safety and integrity of their buildings. We specialize in the installation of firestop systems at penetrations, wall joints, and slab edge joints, as well as providing acoustical sealants, security sealants, architectural caulking, and seismic expansion joints. Since our establishment in 2007, we have been committed to improving the safety and integrity of buildings through our expertise and use of tested and approved firestop systems. Our focus is to deliver exceptional service and quality workmanship to ensure the protection of lives and property.
2. Services we provide:
-Firestopping: T-ratings, CMU Wall Joint, Exterior Caulking, Fireproof Patching, Head of Wall Joints, Through Penetrations, Curtain Wall/Slab Edge, Grease & Fume Duct Protection.
-Expansion Joints: Floor Covers, Roof Covers, Fire Barriers, Vapor Barriers, Wall & Ceiling Covers, Compression Seals, Pre-Compression Foams, Photoluminescent Signage
3. Examples of scope and projects we’ve completed.
4. How to contact us.: https://harborridgeseal.com/contact/
- Social Media Links: https://www.linkedin.com/company/harbor-ridge-sealworks/mycompany/
https://www.instagram.com/harborridgesealworks/?hl=en
https://www.youtube.com/channel/UCq8Lm2TzR5vKpWd9NhYsJ3b/videos
Target Market(s)
Commercial Construction industry
Industry/Entity Type
Commercial Construction industry in California
Coding
Coded - Design and coding required
Number of Pages Required
4 page
Colors
Designer to choose colors to be used in the design.
Requirements
Must have
- 1. Who we are. 2. Services we provide. 3. Examples of scope and projects we’ve completed. 4. How to contact us.
Nice to have
- Logo. Pictures of scope of work and pictures of projects completed or working on.
Should not have
- Names of clients.

```html
<!DOCTYPE html>
<html lang="en">
<head>
<meta charset="utf-8">
<title>Harbor Ridge Sealworks, Inc. — Website Design</title>
<link rel="stylesheet" href="https://fonts.googleapis.com/css2?family=Krona+One&family=Lexend:wght@300;400;500;600;700&family=Oswald:wght@500&display=swap">
<style>
:root{
  --red:#e3141d;
  --blue:#3f55a8;
  --dark:#2a2b30;
  --ink:#1c1d22;
  --gray:#ececec;
  --line:#d9d9d9;
  --white:#ffffff;
  --page:#ffffff;
}
*{box-sizing:border-box;margin:0;padding:0}
html,body{width:1200px;height:2502px;overflow:hidden;background:var(--page)}
body{position:relative;font-family:"Lexend",sans-serif;color:var(--ink)}
.abs{position:absolute}
.screen{position:absolute;background:var(--white);overflow:hidden;border:1px solid #e6e6e6;border-radius:10px}

/* brand */
.logo{position:absolute;display:flex;align-items:center;gap:5px;font-family:"Lexend",sans-serif;font-weight:700;color:var(--red);letter-spacing:.02em;white-space:nowrap}
.logo .mark{border-radius:50%;background:var(--red);flex:none}
.logo.on-dark{color:var(--white)}
.logo.on-dark .mark{background:var(--red)}

.nav{position:absolute;display:flex;align-items:center;gap:16px;font-size:7px;letter-spacing:.04em;color:#444}
.btn{position:absolute;display:flex;align-items:center;justify-content:center;border-radius:3px;font-family:"Lexend",sans-serif;font-weight:700;color:var(--white);letter-spacing:.05em;text-transform:uppercase}
.btn.red{background:var(--red)}
.btn.blue{background:var(--blue)}

.photo{position:absolute}
.hero-photo{background:linear-gradient(100deg,#26272c 0%,#2d2e33 38%,#55575a 58%,#8b8d83 70%,#b9c63a 80%,#5a5d60 100%)}
.hero-title{position:absolute;font-family:"Lexend",sans-serif;font-weight:600;color:var(--white);line-height:1.2}
.hero-sub{position:absolute;font-weight:400;color:#e8e8e8;line-height:1.55}

.octagon{position:absolute;clip-path:polygon(30% 0,70% 0,100% 30%,100% 70%,70% 100%,30% 100%,0 70%,0 30%);background:var(--blue)}
.octagon .fill{position:absolute;inset:2px;clip-path:polygon(30% 0,70% 0,100% 30%,100% 70%,70% 100%,30% 100%,0 70%,0 30%)}
.octagon.soft{background:#e4e4e4}
.octagon.soft .fill{background:var(--white)}
.portrait{background:radial-gradient(circle at 55% 45%,#6a5b4f 0%,#3a3a40 40%,#8c1f24 75%,#b3262b 100%)}

.section-title{position:absolute;font-family:"Krona One",sans-serif;color:var(--ink);text-transform:uppercase;text-align:center;letter-spacing:.02em;line-height:1.2}
.copy p{font-size:7px;line-height:1.35;color:#333;margin-bottom:8px}

.svc-list{position:absolute;list-style:none;font-size:6.6px;font-weight:500}
.svc-list li{height:14.2px}
.svc-list.left{color:var(--red)}
.svc-list.left li::before{content:"›";margin-right:5px}
.svc-list.right{color:var(--blue);text-align:right}
.svc-list.right li::after{content:"‹";margin-left:5px}

.pill{position:absolute;display:flex;align-items:center;justify-content:center;font-family:"Oswald",sans-serif;font-weight:500;color:var(--white);letter-spacing:.02em;border-radius:4px}
.emblem{position:absolute;border-radius:50%;background:var(--white);border:3px solid var(--blue)}
.emblem::after{content:"";position:absolute;inset:22%;border-radius:50%;background:var(--red)}

.proj{position:absolute;border-radius:5px;border:2px solid #f0f0f0}
.mfr{display:flex;align-items:center;justify-content:center;text-align:center}
.mfr .name{font-family:"Lexend",sans-serif;font-weight:700;font-size:10px;color:var(--ink);z-index:1;position:relative}
.arrow{position:absolute;width:11px;height:11px;border-radius:50%;border:1px solid #ccc;display:flex;align-items:center;justify-content:center;font-size:8px;color:#bbb;line-height:1}
.arrow.next{border-color:var(--red);color:var(--red)}

.foot-h{position:absolute;font-size:7px;font-weight:600;color:var(--red);letter-spacing:.05em;text-transform:uppercase}
.foot-list{position:absolute;list-style:none;font-size:6.4px;color:#ddd}
.foot-list li{display:flex;align-items:flex-start;gap:6px;margin-bottom:7px;line-height:1.35}
.ico{width:7px;height:7px;flex:none;margin-top:1px}
.badge{position:absolute;border-radius:50%;border:3px solid var(--white);background:var(--red)}
.badge.square{border-radius:6px;background:#3b3c42}
.social{position:absolute;display:flex;gap:6px}
.social span{width:7px;height:7px;border-radius:1.5px;background:var(--white)}
.input{position:absolute;border:1px solid #666;border-radius:2px;font-size:5.5px;color:#888;padding-left:6px;display:flex;align-items:center}
.accordion{position:absolute;left:8px;right:8px;height:22px;border-bottom:1px solid #555;display:flex;justify-content:space-between;align-items:center;font-size:7px;font-weight:600;color:var(--red);letter-spacing:.05em;text-transform:uppercase}
.accordion i{width:10px;height:10px;border-radius:50%;background:var(--blue);color:var(--white);font-style:normal;font-size:8px;display:flex;align-items:center;justify-content:center}
</style>
</head>
<body>

<!-- ===== Desktop hero preview ===== -->
<section class="screen" style="left:152px;top:73px;width:641px;height:430px">
  <header>
    <div class="logo" style="left:25px;top:15px;font-size:13px"><span class="mark" style="width:14px;height:14px"></span>HARBOR RIDGE SEALWORKS</div>
    <nav class="nav" style="left:305px;top:21px"><span>WHO WE ARE</span><span>WHAT WE DO</span><span>CONTACT</span></nav>
    <div class="btn red" style="left:524px;top:16px;width:92px;height:18px;font-size:6.5px">Quick Inquiry</div>
  </header>
  <div class="photo hero-photo" role="img" aria-label="Technician in a hard hat and high-visibility vest sealing an expansion joint on a concrete deck" style="left:0;top:50px;width:641px;height:340px;clip-path:polygon(0 0,100% 0,100% 80%,40% 97%,0 82%)"></div>
  <svg class="abs" style="left:0;top:0" width="641" height="430" aria-hidden="true">
    <polygon points="0,330 254,380 641,318 620,322 254,405 0,352" fill="var(--red)"/>
  </svg>
  <h1 class="hero-title" style="left:25px;top:128px;font-size:26px">Elevating Fire Safety<br>&amp; Structural Integrity</h1>
  <p class="hero-sub" style="left:25px;top:198px;font-size:8.5px">We are California's Premiere Specialty<br>Firestopping &amp; Seismic Expansion Joint Contractor</p>
  <div class="btn blue" style="left:25px;top:246px;width:82px;height:19px;font-size:6.5px">Contact Us</div>
</section>

<!-- ===== Full desktop home page ===== -->
<section class="screen" style="left:152px;top:546px;width:641px;height:1896px">
  <header>
    <div class="logo" style="left:50px;top:14px;font-size:12px"><span class="mark" style="width:13px;height:13px"></span>HARBOR RIDGE SEALWORKS</div>
    <nav class="nav" style="left:302px;top:20px"><span>WHO WE ARE</span><span>WHAT WE DO</span><span>CONTACT</span></nav>
    <div class="btn red" style="left:507px;top:14px;width:85px;height:17px;font-size:6px">Quick Inquiry</div>
  </header>

  <div class="photo hero-photo" role="img" aria-label="Technician in a hard hat and high-visibility vest sealing an expansion joint on a concrete deck" style="left:0;top:47px;width:641px;height:320px;clip-path:polygon(0 0,100% 0,100% 74%,41% 92%,0 77%)"></div>
  <svg class="abs" style="left:0;top:0" width="641" height="400" aria-hidden="true">
    <polygon points="0,293 264,340 641,283 600,294 264,368 0,305" fill="var(--red)"/>
  </svg>
  <h1 class="hero-title" style="left:50px;top:118px;font-size:24px">Elevating Fire Safety<br>&amp; Structural Integrity</h1>
  <p class="hero-sub" style="left:50px;top:180px;font-size:8px">We are California's Premiere Specialty<br>Firestopping &amp; Seismic Expansion Joint Contractor</p>
  <div class="btn blue" style="left:50px;top:227px;width:76px;height:18px;font-size:6px">Contact Us</div>

  <!-- Who we are -->
  <div class="octagon" style="left:51px;top:406px;width:214px;height:214px"><div class="fill portrait" role="img" aria-label="Smiling firefighter in helmet and turnout gear in front of a fire engine"></div></div>
  <h2 class="section-title" style="left:306px;top:440px;font-size:14px;text-align:left">Who We Are</h2>
  <div class="copy abs" style="left:306px;top:466px;width:272px">
    <p>At Harbor Ridge Sealworks Inc, our mission is to provide our clients with comprehensive firestop and seismic expansion joint solutions that ensure the safety and integrity of their buildings.</p>
    <p>We specialize in the installation of firestop systems at penetrations, wall joints, and slab edge joints, as well as providing acoustical sealants, security sealants, architectural caulking, and seismic expansion joints.</p>
    <p>Since our establishment in 2007, we have been committed to improving the safety and integrity of buildings through our expertise and use of tested and approved firestop systems.</p>
    <p>Our focus is to deliver exceptional service and quality workmanship to ensure the protection of lives and property.</p>
  </div>

  <!-- Services -->
  <svg class="abs" style="left:0;top:0" width="641" height="1100" aria-hidden="true">
    <polygon points="0,658 498,633 641,660 641,1030 498,1015 0,1078" fill="var(--gray)"/>
    <polygon points="66,665 167,688 322,663 167,697" fill="var(--blue)"/>
    <polygon points="331,1047 497,1016 612,1032 497,1024" fill="var(--red)"/>
  </svg>
  <h2 class="section-title" style="left:0;width:641px;top:716px;font-size:14px">Services</h2>
  <div class="pill" style="left:99px;top:774px;width:200px;height:43px;background:var(--red);font-size:16px;padding-right:15px">FIRESTOPPING</div>
  <div class="pill" style="left:345px;top:774px;width:200px;height:43px;background:var(--blue);font-size:16px;padding-left:20px">EXPANSION JOINTS</div>
  <div class="emblem" style="left:287px;top:758px;width:72px;height:72px"></div>
  <div class="octagon soft" style="left:247px;top:838px;width:153px;height:153px"><div class="fill" role="img" aria-label="Worker in an orange safety vest inspecting a floor expansion joint" style="background:linear-gradient(160deg,#c9c9c6,#9a9d9f 55%,#e0792a 80%,#7f8285)"></div></div>
  <ul class="svc-list left" style="left:113px;top:865px">
    <li>T-ratings</li><li>CMU Wall Joint</li><li>Exterior Caulking</li><li>Fireproof Patching</li><li>Head of Wall Joints</li><li>Through Penetrations</li><li>Curtain Wall/Slab Edge</li><li>Grease &amp; Fume Duct Protection.</li>
  </ul>
  <ul class="svc-list right" style="right:111px;top:865px">
    <li>Floor Covers</li><li>Roof Covers</li><li>Fire Barriers</li><li>Vapor Barriers</li><li>Wall &amp; Ceiling Covers</li><li>Compression Seals</li><li>Pre-Compression Foams</li><li>Photoluminescent Signage</li>
  </ul>

  <!-- Completed projects -->
  <h2 class="section-title" style="left:0;width:641px;top:1127px;font-size:14px">Completed Projects</h2>
  <div class="proj" role="img" aria-label="Finished hospital corridor with sealed ceiling joints" style="left:51px;top:1151px;width:135px;height:100px;background:linear-gradient(180deg,#e8ecef,#b9c0c6)"></div>
  <div class="proj" role="img" aria-label="Multi-storey glass office building under blue sky" style="left:51px;top:1258px;width:135px;height:100px;background:linear-gradient(180deg,#4f7fc0,#9db3c9 60%,#d9d3c4)"></div>
  <div class="proj" role="img" aria-label="Stadium seating bowl with completed expansion joints" style="left:193px;top:1151px;width:255px;height:207px;background:linear-gradient(180deg,#8fb0d3 0%,#c9a25a 30%,#3f6fa6 55%,#6b7c8c 100%)"></div>
  <div class="proj" role="img" aria-label="Twin glass towers photographed from a plaza fountain" style="left:455px;top:1151px;width:136px;height:207px;background:linear-gradient(180deg,#7f9fbf,#3e4e5e 60%,#b8c4cc)"></div>
  <div class="btn red" style="left:289px;top:1388px;width:62px;height:17px;font-size:6px">View All</div>
  <div class="abs" style="left:51px;top:1441px;width:540px;height:1px;background:var(--line)"></div>

  <!-- Manufacturers -->
  <h2 class="section-title" style="left:0;width:641px;top:1493px;font-size:14px">Our Manufacturer</h2>
  <div class="arrow" style="left:61px;top:1555px">‹</div>
  <div class="octagon soft mfr" style="left:83px;top:1518px;width:86px;height:86px"><div class="fill"></div><span class="name" style="color:var(--red)">NORVANT</span></div>
  <div class="octagon soft mfr" style="left:180px;top:1518px;width:86px;height:86px"><div class="fill"></div><span class="name">KESTREL</span></div>
  <div class="octagon soft mfr" style="left:279px;top:1518px;width:86px;height:86px"><div class="fill"></div><span class="abs" style="width:46px;height:46px;border-radius:50%;background:var(--red);z-index:1"></span></div>
  <div class="octagon soft mfr" style="left:376px;top:1518px;width:86px;height:86px"><div class="fill"></div><span class="name" style="font-size:9px">ALDER<br>MATERIALS</span></div>
  <div class="octagon soft mfr" style="left:473px;top:1518px;width:86px;height:86px"><div class="fill"></div><span class="name" style="font-size:8.5px;color:var(--blue)">BRIGHTLINE<br>JOINT</span></div>
  <div class="arrow next" style="left:570px;top:1555px">›</div>

  <!-- Footer -->
  <svg class="abs" style="left:0;top:0" width="641" height="1896" aria-hidden="true">
    <polygon points="0,1735 380,1658 641,1735 641,1896 0,1896" fill="var(--dark)"/>
    <polygon points="0,1725 380,1640 641,1725 641,1735 380,1658 0,1735" fill="var(--blue)"/>
    <rect x="0" y="1876" width="641" height="20" fill="var(--red)"/>
  </svg>
  <div class="logo on-dark" style="left:230px;top:1708px;font-size:13px"><span class="mark" style="width:14px;height:14px"></span>HARBOR RIDGE SEALWORKS</div>

  <div class="foot-h" style="left:51px;top:1762px">Contact Info</div>
  <ul class="foot-list" style="left:51px;top:1776px">
    <li><svg class="ico" viewBox="0 0 10 10"><path d="M5 0a3.5 3.5 0 0 1 3.5 3.5C8.5 6 5 10 5 10S1.5 6 1.5 3.5A3.5 3.5 0 0 1 5 0z" fill="var(--red)"/></svg><span>418 W. Marlow Street<br>Anaheim, CA 92801</span></li>
    <li><svg class="ico" viewBox="0 0 10 10"><path d="M2 0l2 2.5-1 1.5a6 6 0 0 0 3 3l1.5-1L10 8l-1.5 2C4 9.5.5 6 0 1.5z" fill="var(--red)"/></svg><span>(555) 210-4410</span></li>
    <li><svg class="ico" viewBox="0 0 10 10"><rect x="1" y="3" width="8" height="6" rx="1" fill="var(--red)"/><rect x="3" y="0" width="4" height="3" fill="var(--red)"/></svg><span>(555) 210-4432</span></li>
    <li><svg class="ico" viewBox="0 0 10 10"><rect x="2.5" y="0" width="5" height="10" rx="1" fill="var(--red)"/></svg><span>(555) 318-2760</span></li>
  </ul>
  <div class="foot-h" style="left:185px;top:1762px">Quick Link</div>
  <ul class="foot-list" style="left:185px;top:1776px">
    <li style="color:var(--red)">Home</li><li>Who We Are</li><li>What We Do</li><li>Contact</li>
  </ul>
  <div class="abs" style="left:185px;top:1838px;font-size:7px;font-weight:600;color:#fff"><span style="color:var(--red)">License</span> #604218</div>
  <div class="foot-h" style="left:301px;top:1762px">Newsletter</div>
  <p class="abs" style="left:301px;top:1776px;font-size:6.3px;color:#ddd;line-height:1.4">Join our newsletter to stay updated<br>about our latest news and articles.</p>
  <div class="input" style="left:301px;top:1803px;width:156px;height:15px">Your email address*</div>
  <div class="btn blue" style="left:301px;top:1824px;width:93px;height:16px;font-size:6px">Subscribe Now</div>
  <div class="badge" style="left:500px;top:1763px;width:30px;height:30px"></div>
  <div class="badge square" style="left:500px;top:1802px;width:30px;height:30px"></div>
  <div class="abs" style="left:51px;top:1881px;font-size:5.6px;color:#fff">© 2023 Harbor Ridge Sealworks. All Right Reserved</div>
  <div class="social" style="left:557px;top:1882px"><span></span><span></span><span></span></div>
</section>

<!-- ===== Mobile home page ===== -->
<section class="screen" style="left:858px;top:73px;width:188px;height:1965px;border-radius:10px">
  <header>
    <div class="logo" style="left:8px;top:13px;font-size:7px"><span class="mark" style="width:9px;height:9px"></span>HARBOR RIDGE SEALWORKS</div>
    <svg class="abs" style="left:162px;top:13px" width="20" height="20" aria-label="Menu" role="img"><circle cx="10" cy="10" r="10" fill="var(--blue)"/><path d="M5 6.5h10M5 10h10M5 13.5h10" stroke="#fff" stroke-width="1.4"/></svg>
  </header>
  <div class="photo hero-photo" role="img" aria-label="Technician in a hard hat and high-visibility vest sealing an expansion joint" style="left:0;top:42px;width:188px;height:150px;clip-path:polygon(0 0,100% 0,100% 82%,38% 96%,0 84%)"></div>
  <svg class="abs" style="left:0;top:0" width="188" height="220" aria-hidden="true">
    <polygon points="0,168 71,186 188,165 175,170 71,198 0,176" fill="var(--red)"/>
  </svg>
  <h1 class="hero-title" style="left:8px;top:72px;font-size:11px">Elevating Fire<br>Safety &amp; Structural<br>Integrity</h1>
  <div class="btn blue" style="left:8px;top:127px;width:85px;height:16px;font-size:5.5px">Contact Us</div>

  <h2 class="section-title" style="left:0;width:188px;top:225px;font-size:11px">Who We Are</h2>
  <div class="octagon" style="left:13px;top:243px;width:164px;height:164px"><div class="fill portrait" role="img" aria-label="Smiling firefighter in helmet and turnout gear"></div></div>
  <div class="copy abs" style="left:8px;top:425px;width:174px">
    <p style="font-size:7.3px;margin-bottom:10px">At Harbor Ridge Sealworks Inc, our mission is to provide our clients with comprehensive firestop and seismic expansion joint solutions that ensure the safety and integrity of their buildings.</p>
    <p style="font-size:7.3px">We specialize in the installation of firestop systems at penetrations, wall joints, and slab edge joints, as well as providing acoustical sealants, security sealants, architectural caulking, and seismic expansion joints.</p>
  </div>
  <div class="btn blue" style="left:8px;top:572px;width:82px;height:19px;font-size:5.8px">Read More</div>

  <!-- Services band -->
  <svg class="abs" style="left:0;top:0" width="188" height="1130" aria-hidden="true">
    <defs><linearGradient id="svcBand" x1="0" y1="0" x2="0" y2="1"><stop offset="0" stop-color="#555a66"/><stop offset=".5" stop-color="#6e3438"/><stop offset="1" stop-color="#3d4a6f"/></linearGradient></defs>
    <polygon points="0,630 140,620 188,623 188,1097 70,1097 0,1112" fill="url(#svcBand)" role="img" aria-label="Background photo of a construction site behind the services list"/>
    <polygon points="10,630 50,640 95,628 50,645" fill="var(--blue)"/>
    <polygon points="120,1090 150,1082 180,1090 150,1086" fill="var(--red)"/>
  </svg>
  <h2 class="section-title" style="left:0;width:188px;top:663px;font-size:11px;color:#fff">Services</h2>
  <div class="abs" style="left:8px;top:691px;width:176px;height:174px;background:rgba(150,40,45,.55);border-radius:6px"></div>
  <div class="pill" style="left:8px;top:691px;width:140px;height:24px;background:var(--red);font-size:13px;justify-content:flex-start;padding-left:12px">FIRESTOPPING</div>
  <div class="emblem" style="left:145px;top:680px;width:40px;height:40px"></div>
  <ul class="svc-list" style="left:20px;top:733px;color:#fff;font-size:7px">
    <li style="height:15.9px">› T-ratings</li><li style="height:15.9px">› CMU Wall Joint</li><li style="height:15.9px">› Exterior Caulking</li><li style="height:15.9px">› Fireproof Patching</li><li style="height:15.9px">› Head of Wall Joints</li><li style="height:15.9px">› Through Penetrations</li><li style="height:15.9px">› Curtain Wall/Slab Edge</li><li style="height:15.9px">› Grease &amp; Fume Duct Protection.</li>
  </ul>
  <div class="abs" style="left:8px;top:880px;width:176px;height:172px;background:rgba(63,85,168,.6);border-radius:6px"></div>
  <div class="pill" style="left:8px;top:880px;width:140px;height:24px;background:var(--blue);font-size:13px;justify-content:flex-start;padding-left:12px">EXPANSION JOINTS</div>
  <div class="emblem" style="left:145px;top:869px;width:40px;height:40px"></div>
  <ul class="svc-list" style="left:20px;top:921px;color:#fff;font-size:7px">
    <li style="height:15.9px">› Floor Covers</li><li style="height:15.9px">› Roof Covers</li><li style="height:15.9px">› Fire Barriers</li><li style="height:15.9px">› Vapor Barriers</li><li style="height:15.9px">› Wall &amp; Ceiling Covers</li><li style="height:15.9px">› Compression Seals</li><li style="height:15.9px">› Pre-Compression Foams</li><li style="height:15.9px">› Photoluminescent Signage</li>
  </ul>

  <!-- Projects -->
  <h2 class="section-title" style="left:0;width:188px;top:1126px;font-size:11px">Completed<br>Projects</h2>
  <div class="arrow" style="left:2px;top:1222px">‹</div>
  <div class="proj" role="img" aria-label="Multi-storey glass office building under blue sky" style="left:17px;top:1168px;width:158px;height:118px;background:linear-gradient(180deg,#4f7fc0,#9db3c9 60%,#d9d3c4)"></div>
  <div class="arrow next" style="left:176px;top:1222px">›</div>
  <div class="btn blue" style="left:61px;top:1300px;width:70px;height:19px;font-size:5.8px">View All</div>
  <div class="abs" style="left:0;top:1348px;width:188px;height:1px;background:var(--line)"></div>

  <h2 class="section-title" style="left:0;width:188px;top:1376px;font-size:11px">Our<br>Manufacturer</h2>
  <div class="arrow" style="left:2px;top:1447px">‹</div>
  <div class="octagon soft mfr" style="left:20px;top:1416px;width:73px;height:73px"><div class="fill"></div><span class="name" style="color:var(--red);font-size:9px">NORVANT</span></div>
  <div class="octagon soft mfr" style="left:101px;top:1416px;width:73px;height:73px"><div class="fill"></div><span class="name" style="font-size:9px">KESTREL</span></div>
  <div class="arrow next" style="left:176px;top:1447px">›</div>
  <div class="btn red" style="left:61px;top:1506px;width:70px;height:19px;font-size:5.8px">View All</div>

  <!-- Mobile footer -->
  <svg class="abs" style="left:0;top:0" width="188" height="1965" aria-hidden="true">
    <polygon points="0,1590 108,1568 188,1590 188,1909 0,1909" fill="var(--dark)"/>
    <polygon points="0,1580 108,1555 188,1580 188,1590 108,1568 0,1590" fill="var(--blue)"/>
    <rect x="0" y="1909" width="188" height="56" fill="var(--red)"/>
  </svg>
  <div class="logo on-dark" style="left:14px;top:1598px;font-size:8px"><span class="mark" style="width:10px;height:10px"></span>HARBOR RIDGE SEALWORKS</div>
  <div class="accordion" style="top:1640px;border-bottom:none">Contact Info <i>−</i></div>
  <ul class="foot-list" style="left:8px;top:1665px;font-size:7px">
    <li><svg class="ico" viewBox="0 0 10 10"><path d="M5 0a3.5 3.5 0 0 1 3.5 3.5C8.5 6 5 10 5 10S1.5 6 1.5 3.5A3.5 3.5 0 0 1 5 0z" fill="var(--red)"/></svg><span>418 W. Marlow Street<br>Anaheim, CA 92801</span></li>
    <li style="margin-top:4px"><svg class="ico" viewBox="0 0 10 10"><path d="M2 0l2 2.5-1 1.5a6 6 0 0 0 3 3l1.5-1L10 8l-1.5 2C4 9.5.5 6 0 1.5z" fill="var(--red)"/></svg><span>(555) 210-4410</span></li>
    <li style="margin-top:4px"><svg class="ico" viewBox="0 0 10 10"><rect x="1" y="3" width="8" height="6" rx="1" fill="var(--red)"/><rect x="3" y="0" width="4" height="3" fill="var(--red)"/></svg><span>(555) 210-4432</span></li>
    <li style="margin-top:4px"><svg class="ico" viewBox="0 0 10 10"><rect x="2.5" y="0" width="5" height="10" rx="1" fill="var(--red)"/></svg><span>(555) 318-2760</span></li>
  </ul>
  <div class="accordion" style="top:1769px;border-top:1px solid #555">Quick Link <i>+</i></div>
  <div class="accordion" style="top:1798px">Newsletter <i>+</i></div>
  <div class="abs" style="left:0;width:188px;text-align:center;top:1840px;font-size:7.5px;font-weight:600;color:#fff"><span style="color:var(--red)">License</span> #604218</div>
  <div class="badge" style="left:24px;top:1862px;width:28px;height:28px"></div>
  <div class="badge square" style="left:108px;top:1862px;width:28px;height:28px"></div>
  <div class="social" style="left:74px;top:1920px"><span></span><span></span><span></span></div>
  <div class="abs" style="left:0;width:188px;text-align:center;top:1935px;font-size:6.5px;color:#fff;line-height:1.5">© 2023 Harbor Ridge Sealworks.<br>All Right Reserved</div>
</section>

</body>
</html>
```